Lantern Bridge - Tax season post card

We need postcard designed for a service firm, The Lantern Bridge LLC primarily for the tax season and also to promote our other service areas. We would like the use of our logo and prefer the orange, green, white color combinations but also open to suggestions. Use the three logos from the attached tax alert flyerThe Lantern Bridge is one stop shop for all your accounting, finance and compliance needs. The firm provides the following services-Accounting & BookkeepingBusiness Advisory Immigration Consulting Income tax preparationIRS RepresentationNon-profit AuditsNotary PublicPayroll and Sales taxLive-Scan fingerprintingProperty ManagementRetirement PlanningThe firm is managed by highly qualified and experienced CPA's, Enrolled Agents, and California Certified Tax Professionals. We give 25% discount for the first time client utilizing our accounting & book-keeping, audit services from your prior year CPA's fees.For the tax season we have $50 discount for our first time clientsTax preparation and consulting include, Trusts, Estates, S-Corp, C-Corp, Partnership, Non-Profit, and Individual Returns2605 Pacific AvenueStockton, CA 95204Phone: 209.463.4436Email: marla.lanternbridge@quillpost.example

Target Market(s)

Businesses and individuals looking for accountant

Industry/Entity Type

Accounting

Font styles to use
Serif

Colors
ec1f27
f37122
ffcf3e

Requirements
Must have
• All services listed
Nice to have
• Attractive logo and fonts
Should not have
• clutter. Too much content tightly adjusted

```html
<!DOCTYPE html>
<html lang="en">
<head>
<meta charset="utf-8">
<title>The Lantern Bridge LLC – Tax Season Postcard</title>
<link href="https://fonts.googleapis.com/css2?family=Crimson+Text:wght@400;600;700&family=Lato:wght@400;700&family=Oswald:wght@500&display=swap" rel="stylesheet">
<style>
:root{
  --bg:#e8e4de;
  --white:#ffffff;
  --green:#8dc63f;
  --orange:#f37122;
  --red:#ec1f27;
  --yellow:#ffcf3e;
  --ink:#231f20;
  --grey-box:#e6e6e6;
  --photo-a:#dfe9f3;
  --photo-b:#8fb8dc;
  --badge-blue:#1f5aa6;
  --badge-navy:#1b3f7a;
}
*{margin:0;padding:0;box-sizing:border-box}
html,body{width:900px;height:1200px;overflow:hidden;background:var(--bg)}
.card{position:absolute;left:108px;width:684px;height:530px;background:var(--white);overflow:hidden}
.card--front{top:63px}
.card--back{top:641px}

/* front */
.front-photo{position:absolute;left:0;top:0}
.brand{position:absolute;left:0;top:98px;width:270px;text-align:center;font-family:"Lato",sans-serif;font-size:15px;color:var(--ink);display:flex;align-items:center;justify-content:center;gap:8px}
.brand__dot{width:14px;height:14px;border-radius:50%;background:var(--orange)}
.headline{position:absolute;left:0;top:128px;width:256px;text-align:center;font-family:"Crimson Text",serif;font-weight:600;font-size:42px;line-height:42px;color:var(--orange)}
.intro{position:absolute;left:0;top:217px;width:290px;height:170px;background:var(--green);padding:12px 14px 0 18px;font-family:"Crimson Text",serif;font-size:16px;line-height:20px;color:var(--ink)}
.intro p{margin-bottom:12px}
.intro p + p{text-align:justify}
.contact-box{position:absolute;left:0;top:405px;width:217px;height:107px;background:var(--orange);border-radius:0 20px 20px 0;padding:18px 0 0 20px;font-family:"Lato",sans-serif;color:var(--white);font-size:17px;line-height:22px;white-space:nowrap}
.contact-box__phone{font-size:22px;font-weight:700;margin-top:4px;display:flex;align-items:center;gap:4px}
.burst{position:absolute;left:228px;top:352px;width:154px;height:154px}
.burst__point{position:absolute;left:22px;top:22px;width:110px;height:110px;background:linear-gradient(#5a5a5a,#2b2b2b)}
.burst__point--2{transform:rotate(22.5deg)}
.burst__point--3{transform:rotate(45deg)}
.burst__point--4{transform:rotate(67.5deg)}
.burst__text{position:absolute;inset:0;display:flex;flex-direction:column;align-items:center;justify-content:center;font-family:"Oswald",sans-serif;font-weight:500;color:var(--orange);font-size:25px;line-height:30px;text-align:center}
.partner{position:absolute}
.partner--filing{left:448px;top:443px;width:114px;height:38px;background:var(--badge-blue);border-radius:20px}
.partner--bank{left:576px;top:443px;width:100px;height:66px;background:var(--badge-navy);opacity:.85;border-radius:8px}
.spanish{position:absolute;left:440px;top:488px;width:130px;text-align:center;font-family:"Lato",sans-serif;font-size:14px;color:var(--ink)}

/* back */
.back-photo{position:absolute;left:0;top:0}
.offer{position:absolute;left:0;top:150px;width:330px;height:120px;background:var(--green);padding:34px 40px 0 20px;font-family:"Crimson Text",serif;font-size:15px;line-height:18px;color:var(--ink)}
.offer p{margin-bottom:5px}
.tab{position:absolute;top:285px;height:28px;background:var(--red);color:var(--white);font-family:"Oswald",sans-serif;font-weight:500;font-size:15px;line-height:28px;padding:0 8px;white-space:nowrap}
.tab--tax{left:8px;width:109px}
.tab--other{left:156px;width:174px;text-align:right}
.list{position:absolute;top:328px;list-style:none;font-family:"Crimson Text",serif;font-size:12.5px;line-height:14.4px;color:var(--ink);white-space:nowrap}
.list--tax{left:14px}
.list--tax li::before{content:"› ";color:var(--orange);font-weight:700}
.list--other{right:356px;text-align:right}
.list--other li::after{content:" ‹";color:var(--orange);font-weight:700}
.rule{position:absolute;left:0;width:330px}
.rule--yellow{top:444px;height:4px;background:var(--yellow)}
.rule--red{top:448px;height:3px;background:var(--red)}
.footer{position:absolute;left:0;top:451px;width:330px;height:79px;background:var(--orange);font-family:"Lato",sans-serif;color:var(--white)}
.footer__left{position:absolute;left:16px;top:20px;line-height:18px;font-size:12.5px;font-weight:700;white-space:nowrap}
.footer__right{position:absolute;right:6px;top:19px;font-weight:400;line-height:14px;font-size:11px;white-space:nowrap}
.footer__right div + div{padding-left:13px}
.footer svg{vertical-align:-2px;margin-right:3px}
.mail-box{position:absolute;background:var(--grey-box)}
.mail-box--stamp{left:524px;top:18px;width:139px;height:139px}
.mail-box--address{left:338px;top:215px;width:325px;height:177px}
</style>
</head>
<body>

<section class="card card--front">
  <svg class="front-photo" width="684" height="530" viewBox="0 0 684 530">
    <defs>
      <linearGradient id="deskTone" x1="0" y1="0" x2="1" y2="1">
        <stop offset="0" stop-color="var(--photo-a)"/>
        <stop offset="1" stop-color="var(--photo-b)"/>
      </linearGradient>
    </defs>
    <circle cx="532" cy="90" r="284" fill="url(#deskTone)" role="img" aria-label="Photo of a hand with a pen reviewing financial charts beside a calculator"/>
    <path d="M259.4,189.2 A290,290 0 0 1 256,0.4" fill="none" stroke="var(--yellow)" stroke-width="12"/>
    <path d="M409.4,352.8 A290,290 0 0 1 259.4,189.2" fill="none" stroke="var(--orange)" stroke-width="14"/>
    <path d="M700,320 A290,290 0 0 1 432.8,362.6" fill="none" stroke="var(--red)" stroke-width="14"/>
  </svg>

  <div class="brand"><span class="brand__dot"></span>The Lantern Bridge, LLC</div>
  <h1 class="headline">Tax Season Alert</h1>

  <div class="intro">
    <p>Let the Lantern Bridge prepare your 2015 Corporate, Individual and all types of tax returns.</p>
    <p>The Lantern Bridge is managed by experienced and highly qualified CPAs and Enrolled IRS agents</p>
  </div>

  <div class="contact-box">
    <div>4817 Hollow Birch Lane</div>
    <div>Stockton, CA 95871</div>
    <div class="contact-box__phone">
      <svg width="16" height="16" viewBox="0 0 24 24"><path d="M6.6 10.8a15 15 0 0 0 6.6 6.6l2.2-2.2c.3-.3.7-.4 1-.2 1.1.4 2.3.6 3.6.6.6 0 1 .4 1 1V20c0 .6-.4 1-1 1A17 17 0 0 1 3 4c0-.6.4-1 1-1h3.5c.6 0 1 .4 1 1 0 1.3.2 2.5.6 3.6.1.3 0 .7-.2 1z" fill="var(--green)"/></svg>
      209-555-0142
    </div>
  </div>

  <div class="burst">
    <div class="burst__point"></div>
    <div class="burst__point burst__point--2"></div>
    <div class="burst__point burst__point--3"></div>
    <div class="burst__point burst__point--4"></div>
    <div class="burst__text">FREE<br>ESTIMATES!</div>
  </div>

  <div class="partner partner--filing"></div>
  <div class="spanish">Se Habla Español</div>
  <div class="partner partner--bank"></div>
</section>

<section class="card card--back">
  <svg class="back-photo" width="330" height="160" viewBox="0 0 330 160">
    <defs>
      <linearGradient id="meetingTone" x1="0" y1="0" x2="1" y2="1">
        <stop offset="0" stop-color="#d9dde2"/>
        <stop offset="1" stop-color="#8a7a6a"/>
      </linearGradient>
    </defs>
    <circle cx="0" cy="-300" r="444" fill="url(#meetingTone)" role="img" aria-label="Photo of a business team meeting around a laptop"/>
    <path d="M335,0 A450,450 0 0 1 258,68.6" fill="none" stroke="var(--yellow)" stroke-width="12"/>
    <path d="M258,68.6 A450,450 0 0 1 93.6,140.2" fill="none" stroke="var(--orange)" stroke-width="12"/>
    <path d="M93.6,140.2 A450,450 0 0 1 -39,148.3" fill="none" stroke="var(--red)" stroke-width="12"/>
  </svg>

  <div class="offer">
    <p>All new, first time clients will receive a special $50 discount for this tax season</p>
    <p>Our office is conveniently located on the Miracle Mile, next to Copperleaf Coffee!</p>
  </div>

  <div class="tab tab--tax">Tax Options:</div>
  <div class="tab tab--other">Other Services Include:</div>

  <ul class="list list--tax">
    <li>Earned Income Credits</li>
    <li>Trusts &amp; Estates</li>
    <li>ITIN</li>
    <li>990, 1120 &amp; 1040</li>
    <li>Rapid refund</li>
    <li>IRS Representation</li>
    <li>Sales Tax and Payroll Taxes</li>
  </ul>
  <ul class="list list--other">
    <li>Business Advisory</li>
    <li>Immigration Consulting</li>
    <li>Non-profit Audits</li>
    <li>Notary Public</li>
    <li>Accounting &amp; Bookkeeping</li>
    <li>Property Management</li>
    <li>Live-Scan fingerprinting</li>
  </ul>

  <div class="rule rule--yellow"></div>
  <div class="rule rule--red"></div>
  <div class="footer">
    <div class="footer__left">
      <div><svg width="12" height="12" viewBox="0 0 24 24"><path d="M6.6 10.8a15 15 0 0 0 6.6 6.6l2.2-2.2c.3-.3.7-.4 1-.2 1.1.4 2.3.6 3.6.6.6 0 1 .4 1 1V20c0 .6-.4 1-1 1A17 17 0 0 1 3 4c0-.6.4-1 1-1h3.5c.6 0 1 .4 1 1 0 1.3.2 2.5.6 3.6.1.3 0 .7-.2 1z" fill="var(--yellow)"/></svg>209-555-0142</div>
      <div><svg width="12" height="12" viewBox="0 0 24 24"><circle cx="12" cy="12" r="10" fill="none" stroke="var(--yellow)" stroke-width="2.5"/><path d="M2 12h20M12 2c3 3 3 17 0 20M12 2c-3 3-3 17 0 20" fill="none" stroke="var(--yellow)" stroke-width="2"/></svg>www.lanternbridge.example</div>
    </div>
    <div class="footer__right">
      <div><svg width="10" height="12" viewBox="0 0 20 24"><path d="M10 0a8 8 0 0 0-8 8c0 6 8 16 8 16s8-10 8-16a8 8 0 0 0-8-8zm0 11a3 3 0 1 1 0-6 3 3 0 0 1 0 6z" fill="var(--yellow)"/></svg>4817 Hollow Birch Lane</div>
      <div>Stockton, CA 95871</div>
    </div>
  </div>

  <div class="mail-box mail-box--stamp"></div>
  <div class="mail-box mail-box--address"></div>
</section>

</body>
</html>
```